Business Card- Redesign and Modernize Existing Card

We are looking to modernize our business card design. We are a home inspection company.
I've attached source file (current business card) .AI file

Ive attached the back of the card information as well. We would like the information on the back of the card to be incorporated in a visual manner, more than just words.

Ive also attached samples of our brochures and other marketing pieces to remain close to brand pattern and color scheme.

We like the black background with blue lettering and the tall cards. Attached an idea as a sample.

Target Market(s)

Real Estate Agents and Home Buyers

Industry/Entity Type

Real Estate

Contact Information for Business Card

Name
Title
Office
Cell Phone
Email
Website
Must Include HOME MOLD TERMITE SEWER AND COMMERCIAL

Requirements
Must have
• Consistent with Brand Color Pattern
Space for headshots
Nice to have
• Watermark Design in the Background Like current business card... not a necessity.

```html
<!DOCTYPE html>
<html lang="en">
<head>
<meta charset="utf-8">
<title>Northvale Group – Business Card</title>
<link rel="stylesheet" href="https://fonts.googleapis.com/css2?family=Montserrat:wght@500;600;800&family=Oswald:wght@400;500&display=swap">
<style>
  :root {
    --backdrop: #dfe5e7;
    --card: #121314;
    --brand-blue: #1e74cc;
    --ink: #f2f2f2;
    --ink-soft: #cfd3d6;
    --star-box: #5e5a58;
    --panel-gray: #3c3c3f;
    --white: #ffffff;
    --badge-gold: #b59a4e;
    --badge-red: #c8312f;
    --badge-yellow: #f2b23a;
    --badge-multi: #3a9bd8;
    --photo-top: #4a5560;
    --photo-bottom: #2a3036;
  }
  * { margin: 0; padding: 0; box-sizing: border-box; }
  html, body {
    width: 955px; height: 1200px; overflow: hidden;
    background: var(--backdrop);
  }
  .card {
    position: absolute; left: 146px; top: 20px;
    width: 662px; height: 1160px;
    background: var(--card);
    overflow: hidden;
    font-family: "Montserrat", sans-serif;
  }
  .brand-mark {
    position: absolute; left: 203px; top: 108px;
    width: 244px; height: 244px; border-radius: 50%;
    background: var(--brand-blue);
  }
  .brand-name {
    position: absolute; left: 0; right: 0; top: 378px;
    text-align: center;
    font-weight: 800; font-size: 42px; letter-spacing: 1px;
    color: var(--brand-blue);
  }
  .rating {
    position: absolute; left: 215px; top: 511px;
    display: flex; gap: 4px;
  }
  .rating .star-box {
    width: 39.6px; height: 39px; background: var(--star-box);
    display: flex; align-items: center; justify-content: center;
  }
  .person-name {
    position: absolute; left: 68px; top: 590px;
    font-weight: 500; font-size: 34px; letter-spacing: 1px;
    color: var(--ink);
  }
  .person-title {
    position: absolute; left: 68px; top: 637px;
    font-weight: 500; font-size: 23px; letter-spacing: 5px;
    color: var(--brand-blue);
  }
  .contact-list {
    position: absolute; left: 74px; top: 695px;
    list-style: none;
    font-family: "Oswald", sans-serif; font-size: 26px; color: var(--ink-soft);
  }
  .contact-list li {
    display: flex; align-items: center; gap: 12px; height: 43px;
  }
  .contact-list svg { width: 24px; height: 24px; fill: var(--brand-blue); }
  .contact-list .web { font-size: 24px; }
  .headshot {
    position: absolute; left: 444px; top: 688px;
    width: 160px; height: 160px; border-radius: 50%;
    border: 4px solid var(--brand-blue);
    background: linear-gradient(180deg, var(--photo-top), var(--photo-bottom));
  }
  .badges { position: absolute; left: 0; top: 880px; width: 662px; height: 90px; }
  .badge { position: absolute; top: 2px; width: 86px; height: 86px; border-radius: 50%; }
  .badge-one { left: 30px; background: var(--badge-gold); }
  .badge-two { left: 137px; background: var(--badge-red); }
  .badge-three { left: 250px; top: 10px; width: 70px; height: 70px; background: var(--badge-yellow); }
  .badge-four { left: 448px; top: 8px; width: 74px; height: 74px; background: var(--badge-multi); }
  .footer-band { position: absolute; left: 0; top: 984px; width: 662px; height: 176px; }
  .footer-email {
    position: absolute; left: 68px; top: 1033px;
    font-family: "Oswald", sans-serif; font-size: 25px; color: var(--white);
  }
  .footer-services {
    position: absolute; left: 68px; top: 1077px;
    font-family: "Oswald", sans-serif; font-weight: 500; font-size: 19px;
    letter-spacing: 1.5px; color: var(--white);
  }
</style>
</head>
<body>
  <main class="card">
    <div class="brand-mark"></div>
    <div class="brand-name">NORTHVALE GROUP</div>

    <div class="rating" aria-label="Five star rating">
      <div class="star-box"><svg width="26" height="26" viewBox="0 0 24 24"><path fill="#fff" d="M12 2l2.9 6.9 7.1.6-5.4 4.7 1.7 7.1L12 17.5 5.7 21.3l1.7-7.1L2 9.5l7.1-.6z"/></svg></div>
      <div class="star-box"><svg width="26" height="26" viewBox="0 0 24 24"><path fill="#fff" d="M12 2l2.9 6.9 7.1.6-5.4 4.7 1.7 7.1L12 17.5 5.7 21.3l1.7-7.1L2 9.5l7.1-.6z"/></svg></div>
      <div class="star-box"><svg width="26" height="26" viewBox="0 0 24 24"><path fill="#fff" d="M12 2l2.9 6.9 7.1.6-5.4 4.7 1.7 7.1L12 17.5 5.7 21.3l1.7-7.1L2 9.5l7.1-.6z"/></svg></div>
      <div class="star-box"><svg width="26" height="26" viewBox="0 0 24 24"><path fill="#fff" d="M12 2l2.9 6.9 7.1.6-5.4 4.7 1.7 7.1L12 17.5 5.7 21.3l1.7-7.1L2 9.5l7.1-.6z"/></svg></div>
      <div class="star-box"><svg width="26" height="26" viewBox="0 0 24 24"><path fill="#fff" d="M12 2l2.9 6.9 7.1.6-5.4 4.7 1.7 7.1L12 17.5 5.7 21.3l1.7-7.1L2 9.5l7.1-.6z"/></svg></div>
    </div>

    <div class="person-name">DANA WHITCOMBE</div>
    <div class="person-title">CERTIFIED MOLD INSPECTOR</div>

    <ul class="contact-list">
      <li><svg viewBox="0 0 24 24"><path d="M12 3L1 12h3v9h6v-6h4v6h6v-9h3z"/></svg>800.555.0142</li>
      <li><svg viewBox="0 0 24 24"><path d="M6.6 10.8a15 15 0 006.6 6.6l2.2-2.2c.3-.3.7-.4 1-.2 1.1.4 2.3.6 3.6.6.6 0 1 .4 1 1V20c0 .6-.4 1-1 1A17 17 0 013 4c0-.6.4-1 1-1h3.5c.6 0 1 .4 1 1 0 1.3.2 2.5.6 3.6.1.3 0 .7-.2 1z"/></svg>555.210.4837</li>
      <li class="web"><svg viewBox="0 0 24 24"><path d="M12 2a10 10 0 100 20 10 10 0 000-20zm-1 17.9A8 8 0 014.1 11L9 16v1a2 2 0 002 2zm6.9-2.5A2 2 0 0016 16h-1v-3a1 1 0 00-1-1H8v-2h2a1 1 0 001-1V7h2a2 2 0 002-2v-.4a8 8 0 012.9 12.8z"/></svg>www.NorthvaleInspect.com</li>
    </ul>

    <div class="headshot" role="img" aria-label="Space for inspector headshot photo"></div>

    <div class="badges" role="img" aria-label="Certification and partner badges">
      <div class="badge badge-one"></div>
      <div class="badge badge-two"></div>
      <div class="badge badge-three"></div>
      <div class="badge badge-four"></div>
    </div>

    <svg class="footer-band" viewBox="0 0 662 176" aria-hidden="true">
      <polygon points="0,18 512,18 620,176 0,176" fill="#3c3c3f"/>
      <polyline points="0,7 527,7 658,172" fill="none" stroke="#1e74cc" stroke-width="9"/>
    </svg>
    <div class="footer-email">dana@northvaleinspect.com</div>
    <div class="footer-services">HOME | MOLD | TERMITE | SEWER | COMMERCIAL</div>
  </main>
</body>
</html>
```